Country House in Italy Needs a Business Card Design

We need a business card design for “Casale del Ginepro”, a modern concept of a Farm Holidays/Country House to be opened in central Italy.
Attached is the company logo you did for us in the past.
Please
- create a double-sided business card design
- on the back I would like to have the logo
- on the front the copy
Copy on card:
o Casale del Ginepro
o Address: Via Pontemurra, 14
Cingoli (MC), Italy
o Website: www.casaledelginepro.it
o Email: info@casaledelginepro.it
o my name : Marisa
o my mobile phone number: +39 347 8123905
In the distribution of information keep in mind the possible inclusion also of a landline telephone number (currently not available / existing).
WE WOULD LIKE TO HAVE A MODERN, PROFFESIONAL, OUT OF THE BOX BUSINESS CARD. BE AS CREATIVE AS YOU WOULD LIKE.

```html
<!DOCTYPE html>
<html lang="en">
<head>
<meta charset="utf-8">
<title>Casale del Ginepro – Business Card</title>
<link rel="stylesheet" href="https://fonts.googleapis.com/css2?family=Cormorant+Garamond:wght@500&family=Oswald:wght@500&family=Montserrat:wght@400;500&family=Oxanium:wght@500&display=swap">
<style>
  :root {
    --stage: #1c1c1c;
    --brown: #5e4330;
    --brown-dark: #4e3727;
    --orange: #f47a3a;
    --white: #ffffff;
    --paper: #f4f4f4;
    --ink: #4a3626;
    --muted: #9a8a7c;
  }
  * { box-sizing: border-box; margin: 0; padding: 0; }
  html, body { width: 1200px; height: 863px; overflow: hidden; }
  body { background: var(--stage); font-family: "Montserrat", sans-serif; position: relative; }

  .card {
    position: absolute;
    width: 560px;
    height: 320px;
    overflow: hidden;
    box-shadow: 0 14px 40px rgba(0,0,0,.55);
  }
  .card svg.card-shapes { position: absolute; inset: 0; }

  .card--back { left: 90px; top: 100px; background: var(--brown); }
  .card--front { left: 550px; top: 443px; background: var(--paper); }

  /* brand name block */
  .brand { position: absolute; display: flex; align-items: center; gap: 12px; }
  .brand-dot {
    width: 56px; height: 56px; border-radius: 50%;
    background: var(--orange);
    flex: none;
  }
  .brand-name {
    font-family: "Cormorant Garamond", serif;
    font-weight: 500;
    font-size: 27px;
    color: var(--ink);
    white-space: nowrap;
  }
  .card--back .brand { left: 34px; top: 150px; }
  .card--front .brand { left: 32px; top: 146px; }

  .website-strip {
    position: absolute; left: 330px; top: 96px;
    color: var(--white); font-size: 13px; font-weight: 500; letter-spacing: .3px;
  }

  /* front card */
  .person { position: absolute; left: 380px; top: 42px; color: var(--white); }
  .person-name {
    font-family: "Oswald", sans-serif; font-weight: 500;
    font-size: 27px; letter-spacing: .5px; text-transform: uppercase; line-height: 1.1;
  }
  .person-role {
    font-size: 9.5px; letter-spacing: 1.2px; text-transform: uppercase; margin-top: 3px;
  }

  .address {
    position: absolute; right: 18px; top: 178px;
    font-family: "Oxanium", sans-serif; font-weight: 500;
    color: var(--white); font-size: 14.5px; line-height: 1.45; text-align: right;
  }

  .contacts { position: absolute; left: 26px; top: 228px; list-style: none; }
  .contacts li {
    display: flex; align-items: center; gap: 8px;
    color: var(--white); font-size: 10.5px; height: 17px;
  }
  .contacts svg { width: 11px; height: 11px; flex: none; fill: var(--white); }
</style>
</head>
<body>

<!-- Back of card -->
<section class="card card--back" aria-label="Business card, back">
  <svg class="card-shapes" viewBox="0 0 560 320" aria-hidden="true">
    <defs>
      <linearGradient id="panelShade" x1="0" y1="0" x2="1" y2="1">
        <stop offset="0" stop-color="#ffffff"/>
        <stop offset="1" stop-color="#e6e6e6"/>
      </linearGradient>
    </defs>
    <path d="M0 70 H282 Q302 70 304 90 L310 240 Q311 262 290 262 H0 Z" fill="url(#panelShade)"/>
  </svg>
  <div class="brand">
    <span class="brand-dot"></span>
    <span class="brand-name">Casale del Ginepro</span>
  </div>
  <p class="website-strip">www.casaledelginepro.it</p>
</section>

<!-- Front of card -->
<section class="card card--front" aria-label="Business card, front">
  <svg class="card-shapes" viewBox="0 0 560 320" aria-hidden="true">
    <defs>
      <linearGradient id="paperShade" x1="0" y1="0" x2="1" y2="0">
        <stop offset="0" stop-color="#f1f1f1"/>
        <stop offset="1" stop-color="#ffffff"/>
      </linearGradient>
    </defs>
    <rect width="560" height="320" fill="url(#paperShade)"/>
    <path d="M0 222 H300 L350 168 H560 V320 H0 Z" fill="var(--brown)"/>
    <path d="M320 0 H560 V148 H405 Q388 148 378 134 L312 28 Q302 0 320 0 Z" fill="var(--orange)"/>
  </svg>

  <div class="person">
    <p class="person-name">Marisa Rinaldi</p>
    <p class="person-role">General Manager</p>
  </div>

  <div class="brand">
    <span class="brand-dot"></span>
    <span class="brand-name">Casale del Ginepro</span>
  </div>

  <p class="address">Via Pontemurra, 14<br>Cingoli (MC), Italy</p>

  <ul class="contacts">
    <li>
      <svg viewBox="0 0 24 24"><path d="M6.6 10.8a15 15 0 0 0 6.6 6.6l2.2-2.2a1 1 0 0 1 1-.25 11.4 11.4 0 0 0 3.6.6 1 1 0 0 1 1 1V20a1 1 0 0 1-1 1A17 17 0 0 1 3 4a1 1 0 0 1 1-1h3.5a1 1 0 0 1 1 1c0 1.25.2 2.45.6 3.6a1 1 0 0 1-.25 1z"/></svg>
      +39 0733 602418
    </li>
    <li>
      <svg viewBox="0 0 24 24"><path d="M7 1h10a2 2 0 0 1 2 2v18a2 2 0 0 1-2 2H7a2 2 0 0 1-2-2V3a2 2 0 0 1 2-2zm0 3v14h10V4zm5 15.5a1.2 1.2 0 1 0 0 2.4 1.2 1.2 0 0 0 0-2.4z"/></svg>
      +39 347 8123905
    </li>
    <li>
      <svg viewBox="0 0 24 24"><path d="M6 2h9l3 3v5h2a2 2 0 0 1 2 2v8a2 2 0 0 1-2 2H4a2 2 0 0 1-2-2v-8a2 2 0 0 1 2-2h2zm2 2v6h8V6h-2V4zm-2 10v2h4v-2zm8 0v2h4v-2z"/></svg>
      +39 0733 602419
    </li>
    <li>
      <svg viewBox="0 0 24 24"><path d="M2 5h20v14H2zm2 2v.5l8 5 8-5V7zm0 2.8V17h16V9.8l-8 5z"/></svg>
      info@casaledelginepro.it
    </li>
    <li>
      <svg viewBox="0 0 24 24"><path d="M12 2a10 10 0 1 0 0 20 10 10 0 0 0 0-20zm6.9 6h-3a15 15 0 0 0-1.3-3.9A8 8 0 0 1 18.9 8zM12 4a13 13 0 0 1 1.9 4h-3.8A13 13 0 0 1 12 4zM4.3 14a8 8 0 0 1 0-4h3.4a16 16 0 0 0 0 4zm.8 2h3a15 15 0 0 0 1.3 3.9A8 8 0 0 1 5.1 16zm3-8h-3a8 8 0 0 1 4.3-3.9A15 15 0 0 0 8.1 8zM12 20a13 13 0 0 1-1.9-4h3.8A13 13 0 0 1 12 20zm2.3-6H9.7a14 14 0 0 1 0-4h4.6a14 14 0 0 1 0 4zm.3 5.9a15 15 0 0 0 1.3-3.9h3a8 8 0 0 1-4.3 3.9zm1.7-5.9a16 16 0 0 0 0-4h3.4a8 8 0 0 1 0 4z"/></svg>
      www.casaledelginepro.it
    </li>
  </ul>
</section>

</body>
</html>
```